Wordpress Design Project for lorettabramwell.com.au

PLEASE NOTE ...Coding Required

I need a simple website to display my art. There will be 4 different categories - FloraGrandis (botanical art), Oceanlife, Travel Sketchbook, Portraits. There needs to be room for an introduction to me and my work,photos of my studio and views from here and a description of each individual piece. I will probably display no more than 10 pieces in category. Obviously I need to change photos on a regular basis.

I would also like to include a Coinvale button to be connected to my Coinvale account.

I have already started to do a website on Wordpress but am finding it too hard to do.

Thank you

Doreen

Reason: I have provided a deadline extension as I feel the initial lead up time could be too short. Hope that helps you. Doreen

Dear designers. Thankyou all so much for submitting some beautiful designs. I will spend time this weekend evaluating them but as the closing date is January 19, I will not make final decisions until then.  You have probably received an update by now butI  just want to mention that Coding is required.

Cheers

Doreen

Thank you Designers for your patience.  I have been advised by PixelHarbor that I cannot make a decision until the deadline has passed, so will let you know on Saturday.

Thank you.
Doreen.

Target Market(s)

35 to 75 who want to buy art and very personal gifts

Industry/Entity Type

Travel

Requirements
Must have
• Ability to change photos often. Modern, elegant, streamlined
Nice to have
• The colour green, an elegant font - sans serif and definitely not courier; room for a photo of me (maybe), and an interesting headline font
Should not have
• quirky, cartooney, retro.

```html
<!DOCTYPE html>
<html lang="en">
<head>
<meta charset="utf-8">
<title>Doreen Bramwell — Art</title>
<link href="https://fonts.googleapis.com/css2?family=Arvo:wght@400;700&family=Roboto+Condensed:wght@700&family=Arimo:ital,wght@0,400;0,700;1,400&display=swap" rel="stylesheet">
<style>
:root{
  --header-green:#3c6313;
  --header-active:#4c7a1c;
  --hero-olive:#7b8a25;
  --hero-frame:#66761a;
  --page-cream:#f4f5e6;
  --heading-olive:#7a8022;
  --caption-olive:#7d8224;
  --dark-tab:#262626;
  --footer:#232323;
  --text-dark:#333333;
  --rule:#c8c9b4;
}
*{margin:0;padding:0;box-sizing:border-box}
html,body{width:1152px;height:1200px;overflow:hidden}
body{position:relative;background:var(--page-cream);font-family:"Arimo",Arial,sans-serif;color:var(--text-dark)}
.abs{position:absolute}

.site-header{left:0;top:0;width:1152px;height:123px;background:var(--header-green)}
.site-title{left:124px;top:44px;font-family:"Arvo",serif;font-weight:700;font-size:32px;letter-spacing:1px;color:#fff;text-shadow:2px 2px 2px rgba(0,0,0,.45);white-space:nowrap}
.nav-active{left:612px;top:0;width:83px;height:121px;background:var(--header-active)}
.nav-pointer{left:646px;top:111px}
.nav-link{top:53px;font-family:"Roboto Condensed",sans-serif;font-weight:700;font-size:13px;color:#fff}

.hero{left:0;top:123px;width:1152px;height:365px;background:var(--hero-olive)}
.portrait-frame{left:125px;top:153px;width:307px;height:307px;background:var(--hero-frame)}
.portrait-photo{left:134px;top:162px;width:289px;height:289px;background:linear-gradient(160deg,#d9d9d6,#8b7d72 55%,#4b5f84)}
.hero-title{left:461px;top:156px;font-family:"Arvo",serif;font-weight:700;font-size:33px;color:#fff;text-shadow:2px 2px 2px rgba(0,0,0,.4)}
.hero-text{left:462px;width:566px;font-style:italic;font-size:13.2px;line-height:17.3px;color:#fff;text-shadow:1px 1px 1px rgba(0,0,0,.35);text-align:justify}
.slide-arrow{top:277px;width:30px;height:47px;background:#1e1e1e;display:flex;align-items:center;justify-content:center}

.section-title{left:118px;font-family:"Arvo",serif;font-weight:700;font-size:22px;color:var(--heading-olive)}
.rule{left:115px;width:922px;border-top:1px dashed #b9bb9c}

.work-tile{top:582px;width:221px;height:236px}
.work-art{left:0;top:0;width:221px;height:195px}
.work-caption{left:0;top:195px;width:221px;height:41px;background:var(--caption-olive);font-family:"Arvo",serif;font-size:16.5px;color:#fff;padding:11px 0 0 11px}
.work-go{right:0;top:0;width:39px;height:41px;background:var(--dark-tab);display:flex;align-items:center;justify-content:center}

.post{top:914px;width:290px}
.post-title{left:2px;top:0;font-size:13.5px;font-weight:700;white-space:nowrap}
.post-avatar{left:0;top:32px;width:60px;height:60px;background:linear-gradient(180deg,#e9e3dc,#c79a84 55%,#2c2c2c)}
.post-excerpt{left:73px;top:32px;width:217px;font-size:11.3px;line-height:13.8px;text-align:justify}
.post-rule{left:0;width:290px;border-top:1px solid var(--rule)}
.post-meta{left:0;top:116px;width:290px;font-size:11.6px;font-weight:700;display:flex;justify-content:space-between}
.post-meta .more{color:var(--heading-olive)}

.site-footer{left:0;top:1094px;width:1152px;height:106px;background:var(--footer)}
.social{top:1110px;width:24px;height:24px;border-radius:50%;background:#0c0c0c;border:1px solid #3a3a3a}
.copyright{left:116px;top:1160px;font-size:12px;color:#e6e6e6}
.pay-name{left:930px;top:1115px;font-size:22px;font-weight:700;color:#3d8fd6}
.card{top:1155px;width:33px;height:20px;border-radius:2px}
</style>
</head>
<body>

<header class="abs site-header">
  <div class="abs nav-active"></div>
  <svg class="abs nav-pointer" width="16" height="10" viewBox="0 0 16 10"><path d="M0 10 L8 0 L16 10Z" fill="#7b8a25"/></svg>
  <h1 class="abs site-title">DOREEN BRAMWELL</h1>
  <nav>
    <span class="abs nav-link" style="left:638px">HOME</span>
    <span class="abs nav-link" style="left:718px">WORK</span>
    <span class="abs nav-link" style="left:799px">SKILLS</span>
    <span class="abs nav-link" style="left:884px">BLOG</span>
    <span class="abs nav-link" style="left:961px">CONTACT</span>
  </nav>
</header>

<section class="abs hero"></section>
<div class="abs portrait-frame"></div>
<div class="abs portrait-photo" role="img" aria-label="Portrait photo of the artist seated"></div>
<h2 class="abs hero-title">Welcome to my site</h2>
<p class="abs hero-text" style="top:225px">Sed ut perspiciatis unde omnis iste natus error sit voluptatem accusantium doloremque laudantium, totam rem aperiam, eaque ipsa quae ab illo inventore veritatis et quasi architecto beatae vitae dicta sunt explicabo. Nemo enim ipsam voluptatem quia voluptas sit aspernatur aut odit aut fugit, sed quia consequuntur magni dolores eos qui ratione voluptatem sequi nesciunt. Neque porro quisquam est, qui dolorem ipsum quia dolor sit amet, consectetur, adipisci velit, sed quia non numquam eius modi tempora incidunt ut labore et dolore magnam aliquam quaerat voluptatem.</p>
<p class="abs hero-text" style="top:363px">Ut enim ad minima veniam, quis nostrum exercitationem ullam corporis suscipit laboriosam, nisi ut aliquid ex ea commodi consequatur? Quis autem vel eum iure reprehenderit qui in ea voluptate velit esse quam nihil molestiae consequatur, vel illum qui dolorem eum fugiat quo voluptas nulla pariaturnisi ut aliquid ex ea commodi consequatur? Quis autem vel eum iure reprehenderit qui in ea voluptate</p>
<div class="abs slide-arrow" style="left:0"><svg width="12" height="20" viewBox="0 0 12 20"><path d="M10 2 L3 10 L10 18" stroke="#fff" stroke-width="3" fill="none"/></svg></div>
<div class="abs slide-arrow" style="left:1122px"><svg width="12" height="20" viewBox="0 0 12 20"><path d="M2 2 L9 10 L2 18" stroke="#fff" stroke-width="3" fill="none"/></svg></div>

<h2 class="abs section-title" style="top:506px">FEATURED WORKS</h2>
<div class="abs rule" style="top:552px"></div>

<article class="abs work-tile" style="left:114px">
  <div class="abs work-art" role="img" aria-label="Watercolour of a red hibiscus flower" style="background:linear-gradient(160deg,#f1eeeb,#ee8b72 45%,#f2efec)"></div>
  <div class="abs work-caption">FloraGrandis<div class="abs work-go"><svg width="12" height="20" viewBox="0 0 12 20"><path d="M2 2 L9 10 L2 18" stroke="#8a9030" stroke-width="3" fill="none"/></svg></div></div>
</article>
<article class="abs work-tile" style="left:347px">
  <div class="abs work-art" role="img" aria-label="Watercolour of a daisy among grass" style="background:linear-gradient(150deg,#cfdcb2,#f2f2ea 50%,#a9c08a)"></div>
  <div class="abs work-caption">Oceanlife<div class="abs work-go"><svg width="12" height="20" viewBox="0 0 12 20"><path d="M2 2 L9 10 L2 18" stroke="#8a9030" stroke-width="3" fill="none"/></svg></div></div>
</article>
<article class="abs work-tile" style="left:582px">
  <div class="abs work-art" role="img" aria-label="Sketch of an old stone house with garden" style="background:linear-gradient(180deg,#d8d2c8,#8f7e86 50%,#6f8f4c)"></div>
  <div class="abs work-caption">Travel Sketchbook<div class="abs work-go"><svg width="12" height="20" viewBox="0 0 12 20"><path d="M2 2 L9 10 L2 18" stroke="#8a9030" stroke-width="3" fill="none"/></svg></div></div>
</article>
<article class="abs work-tile" style="left:815px">
  <div class="abs work-art" role="img" aria-label="Botanical painting of green leaves and pink blossoms" style="background:linear-gradient(140deg,#f4f4f0,#4f7a35 45%,#e6a6c0 80%,#f4f4f0)"></div>
  <div class="abs work-caption">Portraits<div class="abs work-go"><svg width="12" height="20" viewBox="0 0 12 20"><path d="M2 2 L9 10 L2 18" stroke="#8a9030" stroke-width="3" fill="none"/></svg></div></div>
</article>

<h2 class="abs section-title" style="top:851px">RECENT BLOG</h2>
<div class="abs rule" style="top:897px"></div>

<article class="abs post" style="left:115px">
  <h3 class="abs post-title">magna aliqua Ut enim ad minim veniam,....</h3>
  <div class="abs post-avatar" role="img" aria-label="Author photo"></div>
  <p class="abs post-excerpt">ectetur adipisicing elit, sed do eiusmod tempor incididunt ut labore et dolore magna aliqua. Ut enim ad minim veniam, quis nostrud exercitation ullamco laboris</p>
  <div class="abs post-rule" style="top:104px"></div>
  <div class="abs post-meta"><span>Posted by Admin</span><span class="more">Read More</span></div>
  <div class="abs post-rule" style="top:143px"></div>
</article>
<article class="abs post" style="left:433px">
  <h3 class="abs post-title">magna aliqua Ut enim ad minim veniam,....</h3>
  <div class="abs post-avatar" role="img" aria-label="Author photo"></div>
  <p class="abs post-excerpt">ectetur adipisicing elit, sed do eiusmod tempor incididunt ut labore et dolore magna aliqua. Ut enim ad minim veniam, quis nostrud exercitation ullamco laboris</p>
  <div class="abs post-rule" style="top:104px"></div>
  <div class="abs post-meta"><span>Posted by Admin</span><span class="more">Read More</span></div>
  <div class="abs post-rule" style="top:143px"></div>
</article>
<article class="abs post" style="left:747px">
  <h3 class="abs post-title">magna aliqua Ut enim ad minim veniam,....</h3>
  <div class="abs post-avatar" role="img" aria-label="Author photo"></div>
  <p class="abs post-excerpt">ectetur adipisicing elit, sed do eiusmod tempor incididunt ut labore et dolore magna aliqua. Ut enim ad minim veniam, quis nostrud exercitation ullamco laboris</p>
  <div class="abs post-rule" style="top:104px"></div>
  <div class="abs post-meta"><span>Posted by Admin</span><span class="more">Read More</span></div>
  <div class="abs post-rule" style="top:143px"></div>
</article>

<footer class="abs site-footer"></footer>
<div class="abs social" style="left:115px"></div>
<div class="abs social" style="left:147px"></div>
<div class="abs social" style="left:179px"></div>
<p class="abs copyright">© Copyright 2013 Doreen Bramwell.</p>
<span class="abs pay-name">Coinvale</span>
<div class="abs card" style="left:900px;background:#e8e8e8"></div>
<div class="abs card" style="left:935px;background:#dcdcdc"></div>
<div class="abs card" style="left:970px;background:#5d8fc9"></div>
<div class="abs card" style="left:1004px;background:#f0f0f0"></div>

</body>
</html>
```